Electronics Recycling and IT Asset Disposition Flyer and Brochure Design

We need a 2 side A5 Flyer and 4 side A4 folder( brochure) for our electronics waste recycling and IT asset management and disposition business.
Our business provides free electronics waste recycling for companies, schools, learning institutions,councils, IT companies and government sectors. Many people are ignorant of responsible recycling of electronics which could harm our health if not treated properly.
The list of other services attached in the pdf.
We provide an end to end and tailored solution for our customers from collection, logistics, data sanitisation, remarketing and recycling.

The Flyer should create awareness of responsible electronics recycling and drive the audience to contact us or go to our website to learn more about the company and services.A brief list of services should also be included in the flyer.The goal is to get the audience to contact us to enquire more about our services.

The Brochure should include all the above plus provide more details about the company, processes, services,contact details (fb, linkedin,Twitter). The goal is to convert the audience to customers for recycling and provide other services as added services.

The final design for both flyer and brochure should communicate responsible recycling of electronic scrap and tailored solution for every organisation.

The company website is www.kelvora-scrap.com.au based in Australia. We serve clients nationwide.

Target Market(s)

IT companies, Corporate, schools and learning institutions, government sector

Industry/Entity Type

Recycling

Contact Information for Business Card

Name: Derek Ollinfeld
email: derek@kelvora-scrap.com.au
website: www.kelvora-scrap.com.au
mobile: +614 631 02957
Phone: 1300 64 2835

Font styles to use
Serif

Requirements
Must have
• I would like the designs to have more images and icons
Nice to have
Should not have
• none

```html
<!DOCTYPE html>
<html lang="en">
<head>
<meta charset="utf-8">
<title>Kelvora – Brochure Cover</title>
<link rel="stylesheet" href="https://fonts.googleapis.com/css2?family=Open+Sans:wght@400;600;700&display=swap">
<style>
  :root {
    --backdrop: #a7a6ae;
    --paper: #ffffff;
    --paper-shade: #f1f1f1;
    --green: #1f9a4e;
    --green-deep: #0f7f3a;
    --green-light: #39a85f;
    --ink: #2f2f2f;
  }
  html, body {
    margin: 0;
    padding: 0;
    width: 1200px;
    height: 900px;
    overflow: hidden;
    background: var(--backdrop);
    font-family: "Open Sans", Arial, sans-serif;
  }
  .cover {
    position: absolute;
    left: 310px;
    top: 40px;
    width: 580px;
    height: 820px;
    background: linear-gradient(180deg, var(--paper) 0%, var(--paper) 70%, var(--paper-shade) 100%);
    overflow: hidden;
    box-shadow: 0 2px 10px rgba(0,0,0,0.12);
  }
  .cover__band {
    position: absolute;
    left: 0;
    top: 44px;
    width: 470px;
    height: 104px;
    background: linear-gradient(90deg, var(--green-deep) 0%, var(--green) 60%, var(--green-light) 100%);
    border-radius: 0 52px 0 0;
  }
  .cover__photo {
    position: absolute;
    left: 0;
    top: 148px;
    width: 100%;
    height: 348px;
    background:
      radial-gradient(ellipse at 70% 65%, rgba(70,140,70,0.85) 0%, rgba(70,140,70,0) 35%),
      radial-gradient(ellipse at 20% 55%, rgba(170,170,170,0.8) 0%, rgba(170,170,170,0) 30%),
      radial-gradient(ellipse at 30% 20%, rgba(150,120,70,0.7) 0%, rgba(150,120,70,0) 35%),
      linear-gradient(135deg, #5a4544 0%, #6e4a4f 40%, #4d3a3c 70%, #3b3436 100%);
  }
  .cover__badge {
    position: absolute;
    right: 22px;
    top: 50px;
    width: 150px;
    height: 150px;
    border-radius: 50%;
    background: var(--paper);
    box-shadow: inset 0 0 0 6px var(--paper), inset 0 0 0 7px var(--green);
    display: flex;
    align-items: center;
    justify-content: center;
  }
  .cover__brand {
    font-weight: 700;
    font-size: 28px;
    color: var(--green);
  }
  .cover__headline {
    position: absolute;
    left: 0;
    right: 0;
    top: 528px;
    margin: 0;
    text-align: center;
    font-weight: 600;
    font-size: 26px;
    line-height: 1.25;
    color: var(--ink);
  }
  .cover__web {
    position: absolute;
    left: 50%;
    top: 620px;
    transform: translateX(-50%);
    width: 320px;
    height: 28px;
    background: var(--green);
    color: var(--paper);
    font-size: 12px;
    letter-spacing: 3px;
    line-height: 28px;
    text-align: center;
  }
</style>
</head>
<body>
  <section class="cover">
    <div class="cover__band"></div>
    <div class="cover__photo" role="img" aria-label="Close-up photo of discarded computer circuit boards, heatsinks and expansion cards"></div>
    <div class="cover__badge"><span class="cover__brand">Kelvora</span></div>
    <h1 class="cover__headline">BE RESPONSIBLE TODAY FOR<br>A BETTER FUTURE TOMORROW</h1>
    <div class="cover__web">www.kelvora-scrap.com.au</div>
  </section>
</body>
</html>
```